Vorrel Sports Nutrition Brand needs a Packaging label

Hi all, please see the considerations for our vision.
We need a Golden Ratio packaging label design for new Sports nutrition/supplement brand. I would like to give you a little bit of background about myself and hopefully that will help you in creating the design.
I am myself into fitness. I am 33 years old at the moment and been hitting gyms consistently from 14 years old. I do use supplements of all types that helps with performance and body compositions.
Ideally I would like the brand to be able to resonate with male and female audience. The brand needs to give premium look and feel. Those people who will be associating themselves with the brand should be proud of themselves being a part of the team. That's our ideal customer persona.
In terms of colours we are open to your suggestions but do think that red should be included as a detail colour.
P.S Please check out my Instagram to learn more about ideal customer for the brand. @pamodeyxx
When creating the name ''vorrel'' we wanted the name to capture two things. First a feeling that we get when we go to gyms and the feeling is excited. And secondly the name for the product or the industry and that's nutrition. We then shortened the feeling excited to Vorrel for a more catchy name.

The Nutrition information will be sent to add once we pick the design.
The pictures of brands that we admire them are attached.

Please design One label design and just resize for these products. For dimensions please refer to the Print guide attached.
Bulk Core Builder 2.25KG
Tasty Creatine 250G
Vigor Lift Prime 120 Tabs
Surge Flow Pre Workout 250G
Branded Shakers

Target Market(s)

Fitness / bodybuilding audience male & female mass market

Industry/Entity Type

Nutrition

Colors

Designer to choose colors to be used in the design.

Requirements
Must have
• Our logo.
• Please find it attached
Nice to have
• The transparent Logo X some where in the background almost like a watermark. In other words like a subconscious clue.
Should not have
• Organic look.

```html
<!DOCTYPE html>
<html lang="en">
<head>
<meta charset="utf-8">
<title>Vorrel Nutrition – Mass Gainer Label</title>
<link rel="stylesheet" href="https://fonts.googleapis.com/css2?family=Anton&family=Open+Sans:ital,wght@0,400;0,600;0,700;1,400;1,600&family=Oswald:wght@500;600&family=Saira+Semi+Condensed:wght@400;600;700&display=swap">
<style>
  :root {
    --page: #ffffff;
    --label-dark: #1c1c1e;
    --label-mid: #2a2a2d;
    --ink: #ffffff;
    --ink-soft: #d8d8d8;
    --ink-muted: #cfcfcf;
    --red: #d0201f;
    --red-deep: #9e1414;
    --silver-light: #f2f2f2;
    --silver-dark: #9a9a9a;
    --vegan-green: #3fae3a;
    --accent-cyan: #3bc3e0;
  }
  * { margin: 0; padding: 0; box-sizing: border-box; }
  html, body { width: 1200px; height: 560px; overflow: hidden; background: var(--page); }
  body { font-family: "Open Sans", Arial, sans-serif; color: var(--ink); }

  .label { position: relative; width: 1200px; height: 560px; overflow: hidden; }
  .label-body {
    position: absolute; left: 44px; top: 44px; width: 1112px; height: 482px;
    background: radial-gradient(ellipse at 40% 55%, var(--label-mid) 0%, var(--label-dark) 70%);
  }
  .label-texture {
    position: absolute; left: 44px; top: 44px; width: 1112px; height: 482px;
    background: linear-gradient(135deg, rgba(255,255,255,0.02), rgba(255,255,255,0.06) 50%, rgba(255,255,255,0.02));
  }
  .top-band { position: absolute; left: 0; top: 0; width: 1200px; height: 90px; }
  .abs { position: absolute; }

  /* left panel */
  .about-title {
    left: 58px; top: 75px; width: 246px; text-align: center;
    font-weight: 600; font-size: 17.5px; letter-spacing: 0.3px;
  }
  .about-text {
    left: 58px; width: 247px; font-size: 10.2px; line-height: 14.1px;
    text-align: justify;
  }
  .about-text b { font-weight: 600; }
  .usage { left: 58px; top: 390px; width: 247px; font-size: 9.2px; line-height: 13px; text-align: justify; }
  .disclaimer { left: 58px; top: 457px; width: 252px; font-size: 5.5px; line-height: 9px; color: var(--ink-soft); }
  .quality-badge {
    left: 316px; top: 460px; width: 57px; height: 32px; border-radius: 4px;
    background: linear-gradient(180deg, var(--silver-light), var(--silver-dark));
    border: 1px solid #666;
  }

  /* brand column */
  .brand-name {
    left: 436px; top: 322px; transform: translate(-50%, -50%) rotate(-90deg);
    font-family: "Anton", Impact, sans-serif; font-size: 120px; line-height: 1;
    letter-spacing: 8px; color: var(--ink); white-space: nowrap;
  }

  /* product title */
  .product-title {
    left: 618px; top: 88px; width: 166px; text-align: center;
    font-family: "Anton", Impact, sans-serif; line-height: 1;
  }
  .product-title .word-main { display: block; font-size: 66px; color: #f1f1f1; letter-spacing: 1px; }
  .product-title .word-accent { display: block; font-size: 52px; margin-top: -6px; color: var(--red); letter-spacing: 1px; }
  .diet-badges { left: 659px; top: 217px; display: flex; gap: 8px; }
  .diet-badge { width: 34px; height: 34px; border-radius: 50%; border: 2px solid var(--vegan-green); background: rgba(63,174,58,0.12); }

  .claim { left: 557px; top: 308px; display: flex; gap: 7px; align-items: flex-start; }
  .claim svg { margin-top: 10px; }
  .claim-text { font-family: "Saira Semi Condensed", sans-serif; font-weight: 600; font-size: 12.5px; line-height: 17px; }
  .macros { left: 586px; top: 362px; list-style: none; }
  .macros li {
    display: flex; align-items: center; gap: 7px; height: 16px;
    font-family: "Saira Semi Condensed", sans-serif; font-weight: 400; font-size: 12.5px; letter-spacing: 0.3px;
  }
  .macros b { font-weight: 700; margin-left: 2px; }

  .flavour-strip { left: 548px; top: 466px; width: 205px; height: 33px; }
  .flavour-name {
    height: 15px; background: linear-gradient(90deg, #ffffff 70%, #cfcfcf);
    color: var(--red-deep); font-family: "Saira Semi Condensed", sans-serif; font-weight: 700;
    font-size: 12.5px; line-height: 15px; padding-left: 3px;
  }
  .flavour-type {
    height: 17px; margin-top: 1px; background: linear-gradient(90deg, var(--red) 60%, var(--red-deep));
    color: #fff; font-family: "Saira Semi Condensed", sans-serif; font-weight: 700;
    font-size: 11.5px; line-height: 17px; padding-left: 3px;
  }
  .net-weight {
    left: 756px; top: 471px; width: 112px; height: 25px; border-radius: 4px;
    background: linear-gradient(180deg, #ffffff, #bfbfbf); border: 1px solid #777;
    color: #111; font-family: "Oswald", sans-serif; font-weight: 600; font-size: 15px;
    display: flex; align-items: center; justify-content: center; gap: 3px;
  }
  .net-weight span { background: var(--red); color: #fff; padding: 0 2px; line-height: 17px; border-radius: 2px; }

  /* nutrition panel */
  .info-title { left: 889px; top: 79px; width: 242px; text-align: center; font-weight: 600; font-size: 18px; }
  .serving { left: 889px; top: 112px; font-size: 10.5px; line-height: 15px; }
  .serving b { font-weight: 700; }
  .nutrition-table { left: 889px; top: 149px; width: 241px; border-collapse: collapse; font-size: 9.8px; }
  .nutrition-table caption { text-align: right; font-style: italic; font-size: 7.5px; }
  .nutrition-table th { font-weight: 600; font-size: 8.2px; text-align: right; padding-bottom: 1px; border-bottom: 1px solid #bbb; }
  .nutrition-table td { text-align: right; height: 16.6px; padding: 0; font-weight: 600; }
  .nutrition-table td:first-child { text-align: left; }
  .nutrition-table tr.sub td { font-style: italic; font-weight: 400; }
  .nutrition-table tr.sub td:first-child { padding-left: 10px; }
  .nutrition-table tr.rule td { border-bottom: 1px solid #bbb; }
  .nutrition-table tr.first td { padding-top: 12px; height: 24px; }
  .ingredients { left: 889px; top: 335px; width: 242px; font-size: 7.4px; line-height: 10px; }
  .ingredients h3 { font-size: 7.4px; font-weight: 700; }
  .note { left: 889px; width: 242px; font-size: 5.5px; line-height: 7.5px; color: var(--ink-soft); }
  .note b { font-weight: 700; }
  .product-type { left: 888px; top: 507px; width: 258px; height: 12px; }
  .product-type text { font-family: "Open Sans", Arial, sans-serif; font-size: 8px; fill: var(--ink-muted); }
</style>
</head>
<body>
<main class="label">
  <div class="label-body"></div>
  <div class="label-texture" role="img" aria-label="Subtle dark chevron background pattern"></div>

  <svg class="top-band" viewBox="0 0 1200 90" aria-hidden="true">
    <defs>
      <linearGradient id="silver" x1="0" x2="1">
        <stop offset="0" stop-color="#8a8a8a"/>
        <stop offset="0.5" stop-color="#f4f4f4"/>
        <stop offset="1" stop-color="#c8c8c8"/>
      </linearGradient>
    </defs>
    <path d="M176 32 H1156 V68 C900 66 500 60 330 64 C280 65 240 55 176 32 Z" fill="url(#silver)"/>
    <path d="M44 40 C130 36 200 44 330 64 L44 64 Z" fill="var(--label-dark)"/>
    <path d="M44 42 C140 36 210 40 330 62" fill="none" stroke="var(--red)" stroke-width="4"/>
  </svg>

  <h2 class="abs about-title">MASS GAINER</h2>
  <p class="abs about-text" style="top:107px;"><b>MASS GAINER</b> provides your body with a precise combination of high quality proteins blended with ‘slow-releasing’ complex carbohydrates and fast-acting high glycaemic carbohydrates for rapid glycogen replenishment. <b>MASS GAINER</b> also delivers a full spectrum of amino acids for an enhanced post-workout recovery.</p>
  <p class="abs about-text" style="top:220px;"><b>MASS GAINER</b> is a premium quality formula designed to help add high quality calories to your daily diet without compromising protein content and building lean muscle mass without putting on fat.</p>
  <p class="abs about-text" style="top:304px;">It is easy to mix, tastes great and has been engineered for rapid absorption which makes it perfect as a post-workout recovery drink. Every shake contains the full range of nutrients your body needs to repair and build muscle tissue.</p>
  <p class="abs usage">SUGGESTED USE: Add 1 scoop to a shaker or blender, together with 300ml water or milk (full fat milk can be used for extra calories) and consume 1-2 shakes daily, or as required.</p>
  <p class="abs disclaimer">DISCLAIMER: this product is not categorised as a herbal medicine, it is sold as a food supplement. The statement contained on this label does not imply that this product has any medicinal properties, use or efficacy. This product should not be used as a substitute for a varied and balanced diet and do not exceed recommended daily dose. Store in a cool dry place and keep out of reach of young children.</p>
  <div class="abs quality-badge" role="img" aria-label="Quality badge"></div>

  <div class="abs brand-name">VORREL</div>

  <h1 class="abs product-title"><span class="word-main">MASS</span><span class="word-accent">GAINER</span></h1>
  <div class="abs diet-badges">
    <div class="diet-badge" role="img" aria-label="Vegan badge"></div>
    <div class="diet-badge" role="img" aria-label="Gluten free badge"></div>
  </div>

  <div class="abs claim">
    <svg width="22" height="22" viewBox="0 0 22 22" aria-hidden="true">
      <circle cx="11" cy="11" r="9.5" fill="none" stroke="var(--accent-cyan)" stroke-width="1.8"/>
      <path d="M11 6v10M6 11h10" stroke="var(--accent-cyan)" stroke-width="2"/>
    </svg>
    <p class="claim-text">Advanced post-workout<br>Recovery formula</p>
  </div>
  <ul class="abs macros">
    <li><svg width="13" height="13" viewBox="0 0 13 13" aria-hidden="true"><circle cx="6.5" cy="6.5" r="5.6" fill="none" stroke="#fff" stroke-width="1.2"/><path d="M7.4 2.6 4.2 7h2.3l-.9 3.4L8.8 6H6.5z" fill="#fff"/></svg>PROTEIN <b>32g</b></li>
    <li><svg width="13" height="13" viewBox="0 0 13 13" aria-hidden="true"><circle cx="6.5" cy="6.5" r="5.6" fill="none" stroke="#fff" stroke-width="1.2"/><path d="M7.4 2.6 4.2 7h2.3l-.9 3.4L8.8 6H6.5z" fill="#fff"/></svg>CARBS <b>28g</b></li>
    <li><svg width="13" height="13" viewBox="0 0 13 13" aria-hidden="true"><circle cx="6.5" cy="6.5" r="5.6" fill="none" stroke="#fff" stroke-width="1.2"/><path d="M7.4 2.6 4.2 7h2.3l-.9 3.4L8.8 6H6.5z" fill="#fff"/></svg>KCALS <b>302</b></li>
  </ul>

  <div class="abs flavour-strip">
    <div class="flavour-name">Vanila Flavour</div>
    <div class="flavour-type">Diatary Supplement</div>
  </div>
  <div class="abs net-weight">NET WT. <span>4kg</span></div>

  <h2 class="abs info-title">NUTRITIONAL INFO</h2>
  <p class="abs serving">Serving Size: <b>70g</b> <i>(Approx. one scoop)</i><br>Servings per container: <b>57</b></p>
  <table class="abs nutrition-table">
    <caption>Typical Analysis*</caption>
    <thead><tr><th></th><th>Per Serving</th><th>Per 100g</th></tr></thead>
    <tbody>
      <tr class="first"><td>Energy</td><td>1263kj</td><td>1805kj</td></tr>
      <tr class="rule"><td></td><td>302kcals</td><td>432kcals</td></tr>
      <tr class="rule"><td>Fat</td><td>6.9g</td><td>9.8g</td></tr>
      <tr class="sub rule"><td>of which saturates</td><td>0.01g</td><td>0.02g</td></tr>
      <tr class="rule"><td>Carbohydrates</td><td>28g</td><td>40g</td></tr>
      <tr class="sub rule"><td>of which sugars</td><td>14g</td><td>20g</td></tr>
      <tr class="rule"><td>Protein</td><td>32g</td><td>46g</td></tr>
      <tr class="rule"><td>Salt</td><td>0.14g</td><td>0.2g</td></tr>
    </tbody>
  </table>
  <div class="abs ingredients">
    <h3>INGREDIENTS:</h3>
    <p>Protein Blend: (Whey Protein Concentrate (<b>Milk</b>), <b>Milk</b> Protein, <b>Soya</b> Protein Isolate), Maltodextrin, <b>Oat</b> Flour, Fructose, Flavouring, Natural Colouring, Xanthan Gum, Sweetener: Sucralose.</p>
  </div>
  <p class="abs note" style="top:450px;">*PLEASE NOTE: Nutritional values may vary slightly between flavours.</p>
  <p class="abs note" style="top:465px;"><b>ALLERGEN WARNING:</b> For allergens see ingredients in bold. May also contain: nuts, gluten, egg and peanuts.</p>
  <p class="abs note" style="top:489px;"><b>BEST BEFORE END:</b> See Base of Container.</p>
  <svg class="abs product-type" viewBox="0 0 258 12" aria-label="Powdered food supplement with sweetener">
    <text x="0" y="9.5" textLength="256" lengthAdjust="spacing">POWDERED FOOD SUPPLEMENT WITH SWEETENER</text>
  </svg>
</main>
</body>
</html>
```